Online Sofa/Lounge Business needing a Brochure Design

We need a brochure design for a designer online sofa/lounge retailer.
We are a new company based in Sydney and our aim is to make designer lounges accessible to everyone through our lower pricing scheme due to us being an online retailer with low overheads.
Ideally we would like the brochure to be able to be altered by us once the final design is approved so we can edit and add new designs as they are available and change descriptions, pricing etc. and the main brochure design will remain.
The purpose of this brochure is to show clients in face to face meetings, and also marketing purposes such as letterbox drops.
Attached is a basic outline of what we were aiming for originally and are now ready for a finalised design.
I would like to keep the front cover quite similar to how it is now, simple and elegant. I like the whites and don't think adding in other strong colors is what I am looking for.
Target Market(s)
High End
Industry/Entity Type
Marketing
Requirements
Must have
- The layout shall be A5, with the front cover similar to the design I uploaded. The front page must have the web address at the bottom "corvalhome.com.au"
- The center two pages shall have smaller pictures containing the sofa's that I have uploaded. Preferably spread out a little so they are not touching or overlapping. I would like to keep the inside similar to the front cover in terms of style. Once i feel the design is right I will be adding some text ie; names of designs and a brief description. The bottom of both pages must have the web address "corvalhome.com.au"
- The back cover shall have a large logo and a brief company overview (to be confirmed) and the website address "corvalhome.com.au"

```html
<!DOCTYPE html>
<html lang="en">
<head>
<meta charset="utf-8">
<title>Corval Home — Brochure Cover</title>
<link rel="stylesheet" href="https://fonts.googleapis.com/css2?family=Arimo:wght@400&display=swap">
<style>
  :root {
    --paper: #fdfdf5;
    --ink-block: #262626;
    --ink-name: #1b1b1b;
    --ink-body: #1f2a5a;
    --ink-web: #a9d6e8;
  }
  * { margin: 0; padding: 0; box-sizing: border-box; }
  html, body {
    width: 856px;
    height: 1200px;
    overflow: hidden;
    background: var(--paper);
  }
  .cover {
    position: relative;
    width: 856px;
    height: 1200px;
    background: var(--paper);
    font-family: "Arimo", Helvetica, Arial, sans-serif;
  }
  .brand-square {
    position: absolute;
    left: 304px;
    top: 149px;
    width: 259px;
    height: 258px;
    background: var(--ink-block);
  }
  .brand-name {
    position: absolute;
    left: 304px;
    top: 440px;
    width: 259px;
    font-size: 33px;
    font-weight: 400;
    line-height: 1;
    letter-spacing: 0.04em;
    color: var(--ink-name);
    text-align: center;
    white-space: nowrap;
  }
  .intro {
    position: absolute;
    left: 304px;
    top: 566px;
    width: 255px;
    font-size: 17.2px;
    line-height: 24px;
    color: var(--ink-body);
  }
  .intro span {
    display: block;
    text-align: justify;
    text-align-last: justify;
    white-space: nowrap;
  }
  .web-address {
    position: absolute;
    left: 0;
    top: 1145px;
    width: 856px;
    text-align: center;
    font-size: 12px;
    color: var(--ink-web);
    letter-spacing: 0.01em;
  }
</style>
</head>
<body>
  <main class="cover">
    <div class="brand-square"></div>
    <h1 class="brand-name">CORVAL HOME</h1>

    <p class="intro">
      <span>Lorem ipsum dolor sit amet,</span>
      <span>consectetur adipiscing elit.</span>
      <span>Duis consequat laoreet ali-</span>
      <span>quam. Pellentesque ac fau-</span>
      <span>cibus ipsum, vitae dignissim</span>
      <span>diam. Ut facilisis quam in ele-</span>
      <span>mentum maximus. Phasellus</span>
      <span>varius ex nec turpis placerat</span>
      <span>tincidunt. Pellentesque nec</span>
      <span>vulputate dui, et commodo</span>
      <span>purus. Cras accumsan viver-</span>
      <span>ra odio non vulputate. Nulla</span>
      <span>pulvinar, erat sit amet cursus</span>
      <span>sodales, velit nisi lacinia elit,</span>
      <span>at auctor libero odio id diam.</span>
      <span>Praesent faucibus, ligula sit</span>
      <span>amet suscipit tristique, sapien</span>
      <span>urna iaculis lorem, quis dapi-</span>
      <span>bus ex ante et odio. Etiam</span>
      <span>hendrerit faucibus commo-</span>
      <span>do. Sed nec semper eros.</span>
    </p>

    <p class="web-address">www.corvalhome.com.au</p>
  </main>
</body>
</html>
```